Business Card Design Project

We currently have existing logo. Looking to have nice colorful business cards done.
We would like the name of business, phone, address, email and website

Target Market(s)

25-50

Industry/Entity Type

Business

Requirements
Must have
• We are currently using
Samrakan font for our business name
Rage italic font for tag line..
you may visit our website at www.velmorista.com to get good feel

velmorista means colors in India. google velmorista to get more info

```html
<!DOCTYPE html>
<html lang="en">
<head>
<meta charset="utf-8">
<title>Velmorista Indian Restaurant – Business Card</title>
<link rel="stylesheet" href="https://fonts.googleapis.com/css2?family=Alegreya+Sans:wght@400&display=swap">
<style>
  :root {
    --card-deep: #5c1510;
    --card-glow: #74281f;
    --ink: #ffffff;
    --frame: #e9c9c2;
    --art-tone: #6d2219;
  }
  html, body {
    margin: 0;
    padding: 0;
    width: 1200px;
    height: 693px;
    overflow: hidden;
    background: var(--card-deep);
  }
  .card {
    position: relative;
    width: 1200px;
    height: 693px;
    background: var(--card-deep);
    font-family: "Alegreya Sans", "Candara", sans-serif;
    color: var(--ink);
    overflow: hidden;
  }
  .card__backdrop {
    position: absolute;
    inset: 0;
  }
  .card__frame {
    position: absolute;
    left: 46px;
    top: 46px;
    width: 1108px;
    height: 612px;
    border: 1px solid var(--frame);
    box-sizing: border-box;
  }
  .brand__name {
    position: absolute;
    left: 94px;
    top: 96px;
    margin: 0;
    font-size: 104px;
    font-weight: 400;
    line-height: 1;
    letter-spacing: 1px;
  }
  .brand__tagline {
    position: absolute;
    left: 356px;
    top: 208px;
    margin: 0;
    font-size: 34px;
    font-weight: 400;
    line-height: 1;
  }
  .contact {
    position: absolute;
    font-size: 27px;
    line-height: 1;
    margin: 0;
  }
  .address {
    left: 76px;
    top: 340px;
    font-style: normal;
  }
  .address span {
    display: block;
    height: 51px;
  }
  .phones {
    left: 76px;
    top: 516px;
  }
  .phones__row {
    position: relative;
    height: 51px;
  }
  .phones__value {
    position: absolute;
    top: 0;
  }
  .phones__value--tel { left: 162px; }
  .phones__value--fax { left: 136px; }
  .email {
    right: 122px;
    top: 567px;
  }
  .steam-bowl-art {
    position: absolute;
    left: 801px;
    top: 113px;
    width: 294px;
    height: 401px;
  }
</style>
</head>
<body>
  <div class="card">
    <svg class="card__backdrop" width="1200" height="693" viewBox="0 0 1200 693" aria-hidden="true">
      <defs>
        <linearGradient id="glowFade" x1="0" y1="0" x2="0" y2="1">
          <stop offset="0" stop-color="#7a2b22"/>
          <stop offset="1" stop-color="#6a2019"/>
        </linearGradient>
      </defs>
      <rect width="1200" height="693" fill="var(--card-deep)"/>
      <path d="M0 0 H1200 C1130 8 1090 55 1010 150 C860 330 520 470 0 505 Z" fill="url(#glowFade)"/>
    </svg>

    <div class="card__frame"></div>

    <h1 class="brand__name">velmorista</h1>
    <p class="brand__tagline">Indian Restaurant</p>

    <address class="contact address">
      <span>2418 Marlow Avenue</span>
      <span>Almaden, CA</span>
      <span>95120</span>
    </address>

    <div class="contact phones">
      <div class="phones__row">Telephone:<span class="phones__value phones__value--tel">408.555.0142</span></div>
      <div class="phones__row">Fax:<span class="phones__value phones__value--fax">408.555.0143</span></div>
    </div>

    <p class="contact email">info@velmorista.com</p>

    <svg class="steam-bowl-art" viewBox="0 0 294 401" role="img" aria-label="Line illustration of a steaming bowl">
      <defs>
        <radialGradient id="bowlTone" cx="0.5" cy="0.6" r="0.6">
          <stop offset="0" stop-color="#7a2c23"/>
          <stop offset="1" stop-color="#5c1510" stop-opacity="0"/>
        </radialGradient>
      </defs>
      <rect width="294" height="401" rx="40" fill="url(#bowlTone)"/>
    </svg>
  </div>
</body>
</html>
```